Bref créative
Blue Maple Holdings, LLC
Business cards, stationary and envelopes, electronic stationary (Microsoft Word), email signature
Simple
Peter L. Ward
Managing Member
5180 Halvern Court, Suite A
Carrow Falls, MO 64990
pward@bmholdco.example
Phone, email, and name will change for the additional members of the company.
We also want an electronic email signature, and electronic stationary to be used with Microsoft word.
Stationary and envelopes should tie in the theme of the business cards for a uniform look.
Also looking for a Header only version of the stationary, as well as a full page version (header and footer used for design).
Logo used in a creative way.
Horizontal Black Background
Horizontal ALL Black
Horizontal White Background
Horizontal ALL White
Vertical Black Background
Vertical ALL Black
Vertical White Background
Vertical ALL White

```html
<!DOCTYPE html>
<html lang="en">
<head>
<meta charset="utf-8">
<title>Blue Maple Holdings – Business Card</title>
<link href="https://fonts.googleapis.com/css2?family=Open+Sans:wght@400;600;700&display=swap" rel="stylesheet">
<style>
  :root {
    --backdrop: #e4e2df;
    --card-white: #ffffff;
    --brand-red: #c51f2e;
    --brand-red-dark: #a81523;
    --ink-grey: #4a4a4a;
    --mark-grey: #8c8c8c;
    --rule-grey: #9a9a9a;
    --text-light: #ffffff;
    --text-soft: #fbe3e5;
  }
  html, body {
    margin: 0;
    padding: 0;
    width: 1200px;
    height: 780px;
    overflow: hidden;
    background: var(--backdrop);
    font-family: "Open Sans", Arial, sans-serif;
  }
  .canvas {
    position: relative;
    width: 1200px;
    height: 780px;
    display: flex;
    align-items: center;
    justify-content: center;
  }
  .business-card {
    position: relative;
    width: 900px;
    height: 540px;
    border-radius: 32px;
    overflow: hidden;
    background: var(--card-white);
    box-shadow: 0 6px 18px rgba(0,0,0,0.18);
  }
  .card-top {
    position: absolute;
    inset: 0 0 auto 0;
    height: 306px;
    display: flex;
    align-items: center;
    justify-content: center;
  }
  .brand-lockup {
    display: flex;
    align-items: center;
    gap: 18px;
    margin-top: 10px;
  }
  .brand-dot {
    width: 34px;
    height: 34px;
    border-radius: 50%;
    background: var(--mark-grey);
  }
  .brand-name {
    font-weight: 600;
    font-size: 40px;
    letter-spacing: 0;
    color: var(--ink-grey);
  }
  .card-rule {
    position: absolute;
    left: 0; right: 0;
    top: 306px;
    height: 6px;
    background: var(--rule-grey);
  }
  .card-bottom {
    position: absolute;
    left: 0; right: 0; bottom: 0;
    top: 312px;
    background: linear-gradient(180deg, var(--brand-red) 0%, var(--brand-red-dark) 100%);
    color: var(--text-light);
  }
  .member-info {
    position: absolute;
    right: 468px;
    top: 54px;
    text-align: right;
  }
  .member-name {
    font-weight: 700;
    font-size: 24px;
    margin: 0 0 4px;
  }
  .member-title {
    font-weight: 600;
    font-size: 19px;
    margin: 0 0 16px;
  }
  .member-address {
    font-size: 19px;
    line-height: 1.45;
    margin: 0;
  }
  .divider {
    position: absolute;
    left: 450px;
    top: 52px;
    width: 2px;
    height: 136px;
    background: var(--text-soft);
  }
  .contact-list {
    position: absolute;
    left: 470px;
    top: 48px;
    margin: 0;
    padding: 0;
    list-style: none;
    font-size: 19px;
  }
  .contact-list li {
    display: flex;
    align-items: center;
    gap: 12px;
    height: 35px;
  }
  .contact-icon {
    width: 20px;
    height: 20px;
    flex: none;
  }
</style>
</head>
<body>
<main class="canvas">
  <article class="business-card">
    <header class="card-top">
      <div class="brand-lockup">
        <span class="brand-dot" aria-hidden="true"></span>
        <span class="brand-name">Blue Maple Holdings</span>
      </div>
    </header>
    <div class="card-rule"></div>
    <section class="card-bottom">
      <div class="member-info">
        <p class="member-name">Peter L. Ward</p>
        <p class="member-title">Managing Member</p>
        <p class="member-address">5180 Halvern Court, Suite A<br>Carrow Falls, MO 64990</p>
      </div>
      <div class="divider"></div>
      <ul class="contact-list">
        <li>
          <svg class="contact-icon" viewBox="0 0 20 20" aria-hidden="true"><path d="M5 2 L8 2 L9 6 L7 8 Q9 12 12 13 L14 11 L18 12 L18 15 Q18 18 15 18 Q3 16 2 5 Q2 2 5 2 Z" fill="#fff"/></svg>
          <span>(555) 208-7316</span>
        </li>
        <li>
          <svg class="contact-icon" viewBox="0 0 20 20" aria-hidden="true"><rect x="5" y="1" width="10" height="18" rx="2" fill="#fff"/><rect x="7" y="4" width="6" height="9" fill="#c51f2e"/></svg>
          <span>(555) 640-2195</span>
        </li>
        <li>
          <svg class="contact-icon" viewBox="0 0 20 20" aria-hidden="true"><rect x="5" y="2" width="10" height="6" fill="#fff"/><rect x="2" y="8" width="16" height="7" rx="1" fill="#fff"/><rect x="5" y="13" width="10" height="5" fill="#fff" stroke="#c51f2e" stroke-width="1"/></svg>
          <span>(555) 871-3340</span>
        </li>
        <li>
          <svg class="contact-icon" viewBox="0 0 20 20" aria-hidden="true"><rect x="2" y="4" width="16" height="12" fill="#fff"/><path d="M2 4 L10 11 L18 4" fill="none" stroke="#c51f2e" stroke-width="1.5"/></svg>
          <span>pward@bmholdco.example</span>
        </li>
      </ul>
    </section>
  </article>
</main>
</body>
</html>
```